Movie Showtimes Website needs an updated new look

Website = www.marlovista.com

We want to update the look of our website. We want our website to look modern, trendy, something that was designed in 2018.

We don't need any HTML or CSS or web development. All we need is the graphical prototype, preferably in Photoshop with layers.

Most of our visitors use mobile devices. Our website is RESPONSIVE -- it is flexible to fit all screen sizes.

We will use this new logo (designed on Quillbarn):
https://www.quillbarn.com/design/27364512

Thank you for your kind consideration.

Please find attached 3 PDF files with the current webpages:

1. Each city location has its own HOME PAGE like this:

https://www.marlovista.com/ont/ottawa/

2. The most visited pages have movie SHOWTIMES and look like this:

https://www.marlovista.com/theatres/rovenna-hartfield-vip

MOVIE TITLE (poster + basic info + 4 buttons)
-- the type of the screening (ex. Regular, VYRA, 3D, etc.)
-- individual days and showtimes

3. INFORMATION about movies:

https://www.marlovista.com/movies/silent-copper-road-2018

Thank you.

Target Market(s)

Canada and USA, target audience = ages 13-50

Industry/Entity Type

Movie

Number of Pages Required

3 page

Font styles to use
Sans Serif

Colors

Designer to choose colors to be used in the design.

Requirements
Must have
• - For the main body text (such as movie times, description, information) we prefer dark text on a light background.
• - We will use the new logo https://www.quillbarn.com/design/27364512 -- but the text Marlo Vista in the logo doesn't have to look exactly like that, it can be on the same line and have the same or different size
Should not have
• No more than 2 different fonts (ex. one font for headers and titles, another one for text)

```html
<!DOCTYPE html>
<html lang="en">
<head>
<meta charset="utf-8">
<title>Marlo Vista – Ottawa Home</title>
<link href="https://fonts.googleapis.com/css2?family=Oswald:wght@400;500;600&family=Open+Sans:wght@400;600;700&display=swap" rel="stylesheet">
<style>
:root{
  --blue:#2fa6e0;
  --blue-dark:#1f86bd;
  --ink:#2a2a2a;
  --text:#444;
  --muted:#8a8a8a;
  --line:#e2e2e2;
  --soft:#f3f3f3;
  --page:#ececec;
  --dark:#2d2d2d;
  --footer:#3a3a3a;
  --red:#d32f2f;
  --pink:#e8336d;
  --gold:#f6c21c;
}
*{box-sizing:border-box;margin:0;padding:0}
html,body{width:1200px;height:2504px;overflow:hidden}
body{position:relative;background:var(--page);font-family:"Open Sans",Arial,sans-serif;color:var(--text);font-size:14px}
h2,.tab,.nav a,.btn,.title{font-family:"Oswald","Arial Narrow",sans-serif}

.topbar{position:absolute;left:0;top:0;width:1200px;height:72px;background:var(--dark)}
.logo{position:absolute;left:0;right:0;top:18px;display:flex;justify-content:center;align-items:center;gap:10px}
.logo-dot{width:34px;height:34px;border-radius:50%;background:#fff}
.logo-name{font-family:"Oswald",sans-serif;font-weight:500;font-size:22px;color:#fff;letter-spacing:2px}
.lang{position:absolute;right:112px;top:10px;font-size:11px;color:#ccc}
.login{position:absolute;right:112px;top:38px;font-size:11px;color:#fff;font-weight:700;display:flex;gap:6px;align-items:center}
.login i{width:12px;height:12px;border-radius:50%;background:#fff;display:block}

.mainnav{position:absolute;left:0;top:72px;width:1200px;height:72px;background:var(--blue)}
.nav{position:absolute;left:160px;top:0;height:72px;display:flex;align-items:center;gap:36px}
.nav a{color:#fff;text-decoration:none;font-size:15px;font-weight:500;letter-spacing:1px}
.search{position:absolute;right:140px;top:22px;width:170px;height:28px;background:#fff;border-radius:14px;font-size:11px;color:var(--muted);padding:6px 14px}

.footer{position:absolute;left:0;top:2180px;width:1200px;height:324px;background:var(--footer)}
.panel{position:absolute;left:112px;top:144px;width:976px;height:2136px;background:#fff;box-shadow:0 2px 10px rgba(0,0,0,.15)}

.main{position:absolute;left:20px;top:0;width:668px}
.side{position:absolute;left:708px;top:48px;width:252px}

.crumb{height:24px;margin-top:12px;font-size:11px;color:var(--muted);line-height:24px}
.tabs{display:flex;height:56px;margin-top:12px;border:1px solid var(--line)}
.tab{flex:1;display:flex;align-items:center;justify-content:center;gap:10px;font-size:16px;color:var(--ink)}
.tab.on{background:var(--dark);color:#fff;font-size:20px;letter-spacing:1px}
.tab+.tab{border-left:1px solid var(--line)}

h2{display:flex;align-items:center;gap:10px;font-size:19px;font-weight:500;color:var(--ink);letter-spacing:.5px;margin-top:28px;height:32px;border-bottom:2px solid var(--ink)}
h2::before{content:"";width:10px;height:10px;background:var(--ink)}

.movie{display:flex;height:148px;padding:12px 0;border-bottom:1px solid var(--line);position:relative}
.poster{width:84px;height:124px;border-radius:3px;flex:none}
.minfo{margin-left:18px;flex:1}
.title{font-size:22px;font-weight:500;color:var(--blue-dark);display:flex;align-items:center;gap:8px}
.badge{font-family:"Open Sans",sans-serif;font-size:9px;font-weight:700;color:var(--muted);border:1px solid #bbb;padding:1px 4px;border-radius:2px}
.meta{font-size:12px;color:var(--muted);margin-top:6px}
.rate{position:absolute;right:0;top:16px;width:46px;height:46px;background:var(--soft);border-radius:4px;text-align:center;font-weight:700;font-size:15px;line-height:46px;color:var(--ink)}
.acts{position:absolute;left:102px;right:0;bottom:14px;display:flex;gap:8px}
.btn{flex:1;height:26px;border:1px solid var(--line);border-radius:3px;font-size:11px;color:var(--blue-dark);display:flex;align-items:center;justify-content:center;gap:6px;letter-spacing:.5px}
.btn.solid{color:var(--muted)}

.wide-btn{width:260px;height:36px;margin:26px auto 0;border:1px solid #bbb;border-radius:3px;font-family:"Oswald",sans-serif;font-size:13px;color:var(--ink);display:flex;align-items:center;justify-content:center}

.give{margin-top:44px;height:72px;background:var(--red);display:flex;align-items:center;justify-content:space-between;padding:0 24px;color:#fff}
.give strong{font-family:"Oswald",sans-serif;font-size:30px;font-weight:600;letter-spacing:1px}
.give small{display:block;font-size:10px;opacity:.85}
.give span{font-size:11px;font-weight:700;border:1px solid #fff;padding:8px 14px}

.promos{display:flex;gap:28px;margin-top:16px}
.promo{flex:1;display:flex;gap:14px;height:150px}
.promo .poster{width:100px;height:150px}
.promo h3{font-size:16px;font-weight:700;color:var(--ink)}
.promo p{font-size:11px;color:var(--muted);margin-top:4px;line-height:1.5}
.promo .pill{display:inline-block;margin-top:14px;width:96px;height:28px;border:1px solid var(--blue);border-radius:14px;color:var(--blue);font-size:11px;text-align:center;line-height:26px}

.fav{display:flex;align-items:center;gap:14px;height:64px;border-bottom:1px solid var(--line)}
.fav b{display:block;font-size:16px;color:var(--ink)}
.fav small{font-size:11px;color:var(--muted)}

.deal{margin-top:40px;height:88px;background:var(--gold);display:flex;align-items:center;justify-content:space-between;padding:0 28px 0 130px;position:relative}
.deal .art{position:absolute;left:0;top:0;width:110px;height:88px;background:linear-gradient(135deg,#f7a9c0,#8fc6e8)}
.deal em{font-style:normal;font-weight:700;color:var(--ink);font-size:14px}
.deal strong{font-family:"Oswald",sans-serif;font-size:34px;color:var(--red)}
.deal span{background:var(--blue-dark);color:#fff;font-size:12px;font-weight:700;padding:8px 16px}

.bdays{display:grid;grid-template-columns:repeat(3,1fr);row-gap:14px;margin-top:16px}
.person{display:flex;align-items:center;gap:12px;height:56px}
.avatar{width:52px;height:52px;border-radius:50%;flex:none}
.person b{display:block;font-size:13px;color:var(--ink)}
.person small{font-size:11px;color:var(--muted)}

.ad{border:1px solid var(--line);margin-bottom:20px;overflow:hidden;text-align:center}
.ad-brand{font-family:"Oswald",sans-serif;font-size:26px;font-weight:500;padding:14px 0 8px}
.ad .grid{display:grid;grid-template-columns:1fr 1fr;gap:6px;padding:0 10px}
.ad .grid div{height:212px}
.ad .cta{display:inline-block;margin:8px 0 18px;background:var(--pink);color:#fff;font-size:12px;font-weight:700;padding:7px 18px}
.fly{background:#f5f5f5;padding:22px 16px}
.fly .big{font-family:"Oswald",sans-serif;font-size:54px;color:var(--red);line-height:1}
.fly .cta{background:var(--gold);color:var(--ink)}

.foot-ad{position:absolute;left:176px;top:2312px;width:852px;height:80px;background:#1d3f73;display:flex;align-items:center;color:#fff}
.foot-ad .brand{width:200px;text-align:center;font-family:"Oswald",sans-serif;font-size:28px;background:#fff;color:#1d3f73;height:80px;line-height:80px}
.foot-ad .copy{flex:1;text-align:center}
.foot-ad .copy b{display:block;font-size:20px;letter-spacing:.5px}
.foot-ad .copy small{font-size:12px;letter-spacing:2px;opacity:.8}
.share{position:absolute;left:0;right:0;top:2420px;display:flex;justify-content:center;align-items:center;gap:8px;color:#bbb;font-size:11px;font-weight:700}
.share i{width:20px;height:20px;background:#5a5a5a;display:block}
.links{position:absolute;left:0;right:0;top:2460px;text-align:center;color:#999;font-size:10px}
</style>
</head>
<body>
<header class="topbar">
  <div class="logo"><span class="logo-dot"></span><span class="logo-name">MARLO VISTA</span></div>
  <div class="lang">English | Français</div>
  <div class="login"><i></i>LOG IN</div>
</header>
<nav class="mainnav">
  <div class="nav"><a>CINEMAS</a><a>MOVIES</a><a>TOP 10</a><a>TRAILERS</a><a>UPCOMING</a><a>DVD</a><a>MORE ▾</a></div>
  <div class="search">Search…</div>
</nav>

<div class="footer"></div>

<main class="panel">
  <section class="main">
    <div class="crumb">Ottawa &gt; Home</div>
    <div class="tabs">
      <div class="tab on">MOVIE TIMES!</div>
      <div class="tab"><svg width="20" height="18" viewBox="0 0 20 18"><rect x="1" y="4" width="18" height="13" fill="none" stroke="#2a2a2a" stroke-width="2"/><path d="M1 4 L5 1 L19 1" fill="none" stroke="#2a2a2a" stroke-width="2"/></svg>choose a CINEMA</div>
      <div class="tab"><svg width="20" height="18" viewBox="0 0 20 18"><rect x="1" y="1" width="18" height="16" fill="none" stroke="#2a2a2a" stroke-width="2"/><path d="M8 5 L14 9 L8 13Z" fill="#2a2a2a"/></svg>choose a MOVIE</div>
    </div>

    <h2>NEW MOVIES THIS WEEK</h2>
    <div class="movies">
      <article class="movie">
        <div class="poster" role="img" aria-label="Movie poster for Silent Copper Road" style="background:linear-gradient(160deg,#4a5a8a,#1c1f3a)"></div>
        <div class="minfo"><div class="title">Silent Copper Road <span class="badge">PG</span></div><div class="meta">2h 20 • Sci-Fi Action • Colm Averett, Lia Doran</div></div>
        <div class="rate">7.7</div>
        <div class="acts"><span class="btn">▶ TRAILER</span><span class="btn solid">SHOWTIMES</span><span class="btn solid">REVIEWS</span><span class="btn">BUY TICKETS</span></div>
      </article>
      <article class="movie">
        <div class="poster" role="img" aria-label="Movie poster for Paper Lanterns: A Light Below" style="background:linear-gradient(160deg,#6b4a2a,#1a120c)"></div>
        <div class="minfo"><div class="title">Paper Lanterns: A Light Below <span class="badge">PG</span></div><div class="meta">1h 45 • Drama • Nolan Brisk, Ada Wren</div></div>
        <div class="rate">6.2</div>
        <div class="acts"><span class="btn">▶ TRAILER</span><span class="btn solid">SHOWTIMES</span><span class="btn solid">REVIEWS</span><span class="btn">BUY TICKETS</span></div>
      </article>
      <article class="movie">
        <div class="poster" role="img" aria-label="Movie poster for Quiet Signal 2" style="background:linear-gradient(160deg,#8aa0b8,#2c3a4a)"></div>
        <div class="minfo"><div class="title">Quiet Signal 2 <span class="badge">14A</span></div><div class="meta">1h 52 • Horror • Mira Solent, Jude Farrow</div></div>
        <div class="rate">5.9</div>
        <div class="acts"><span class="btn">▶ TRAILER</span><span class="btn solid">SHOWTIMES</span><span class="btn solid">REVIEWS</span><span class="btn">BUY TICKETS</span></div>
      </article>
      <article class="movie">
        <div class="poster" role="img" aria-label="Movie poster for Isle of Thistles" style="background:linear-gradient(160deg,#d9d2c4,#a33a2a)"></div>
        <div class="minfo"><div class="title">Isle of Thistles <span class="badge">PG</span></div><div class="meta">1h 41 • Animation • Bryce Hollen, Tova Lind</div></div>
        <div class="rate">8.1</div>
        <div class="acts"><span class="btn">▶ TRAILER</span><span class="btn solid">SHOWTIMES</span><span class="btn solid">REVIEWS</span><span class="btn">BUY TICKETS</span></div>
      </article>
      <article class="movie">
        <div class="poster" role="img" aria-label="Movie poster for Ember Crossing" style="background:linear-gradient(160deg,#9a8a74,#3a3128)"></div>
        <div class="minfo"><div class="title">Ember Crossing <span class="badge">14A</span></div><div class="meta">1h 47 • War Drama • Sam Calder, Ewan Pike</div></div>
        <div class="rate">7.4</div>
        <div class="acts"><span class="btn">▶ TRAILER</span><span class="btn solid">SHOWTIMES</span><span class="btn solid">REVIEWS</span><span class="btn">BUY TICKETS</span></div>
      </article>
    </div>
    <div class="wide-btn">Show All Playing Movies ›</div>

    <div class="give"><div><strong>LIFE IS FOUND IN GIVING</strong><small>Kindred Aid • Give today, help tomorrow</small></div><span>FIND A DONATION EVENT</span></div>

    <h2>PROMOTIONS</h2>
    <div class="promos">
      <div class="promo"><div class="poster" role="img" aria-label="Promotional poster for Harbor Nine" style="background:linear-gradient(160deg,#c58a3e,#3b2614)"></div><div><h3>Harbor Nine</h3><p>Win tickets to the premiere<br>this weekend</p><span class="pill">DETAILS</span></div></div>
      <div class="promo"><div class="poster" role="img" aria-label="Promotional poster for Ironvale" style="background:linear-gradient(160deg,#6f8f5a,#1e2a18)"></div><div><h3>Ironvale</h3><p>Enter to win a family<br>movie night pack</p><span class="pill">DETAILS</span></div></div>
    </div>

    <h2>MY FAVOURITE CINEMAS</h2>
    <div class="favs">
      <div class="fav"><svg width="26" height="32" viewBox="0 0 26 32"><path d="M13 1C6.4 1 1 6.2 1 12.6 1 21 13 31 13 31s12-10 12-18.4C25 6.2 19.6 1 13 1z" fill="none" stroke="#2a2a2a" stroke-width="2"/><circle cx="13" cy="12.5" r="4" fill="#2a2a2a"/></svg><div><b>Rovenna Carnival</b><small>140 Elm Row, Ottawa ON • 6 screens</small></div></div>
      <div class="fav"><svg width="26" height="32" viewBox="0 0 26 32"><path d="M13 1C6.4 1 1 6.2 1 12.6 1 21 13 31 13 31s12-10 12-18.4C25 6.2 19.6 1 13 1z" fill="none" stroke="#2a2a2a" stroke-width="2"/><circle cx="13" cy="12.5" r="4" fill="#2a2a2a"/></svg><div><b>Hartfield Forum</b><small>2 Quarry Lane, Ottawa ON • 9 screens</small></div></div>
    </div>
    <div class="wide-btn">Change My Favourite Cinemas ›</div>

    <div class="deal"><div class="art" role="img" aria-label="Shopping deals artwork"></div><em>Find Exclusive Deals<br>Now!</em><strong>Up to 70% off!</strong><span>Learn More</span></div>

    <h2>HAPPY BIRTHDAY</h2>
    <div class="bdays">
      <div class="person"><div class="avatar" role="img" aria-label="Portrait of Jonas Alder" style="background:#b08a70"></div><div><b>Jonas Alder</b><small>52 today</small></div></div>
      <div class="person"><div class="avatar" role="img" aria-label="Portrait of Tobin Marlowe" style="background:#6e4c3a"></div><div><b>Tobin Marlowe</b><small>57 today</small></div></div>
      <div class="person"><div class="avatar" role="img" aria-label="Portrait of Evander Holt" style="background:#9c7a64"></div><div><b>Evander Holt</b><small>45 today</small></div></div>
      <div class="person"><div class="avatar" role="img" aria-label="Portrait of Lenora Fay" style="background:#c9a98c"></div><div><b>Lenora Fay</b><small>96 today</small></div></div>
      <div class="person"><div class="avatar" role="img" aria-label="Portrait of Dev Ransome" style="background:#8a6a58"></div><div><b>Dev Ransome</b><small>49 today</small></div></div>
      <div class="person"><div class="avatar" role="img" aria-label="Portrait of Matteo Sarno" style="background:#a48068"></div><div><b>Matteo Sarno</b><small>55 today</small></div></div>
      <div class="person"><div class="avatar" role="img" aria-label="Portrait of Marisa Pell" style="background:#c09078"></div><div><b>Marisa Pell</b><small>41 today</small></div></div>
      <div class="person"><div class="avatar" role="img" aria-label="Portrait of Clara Windham" style="background:#b48a7c"></div><div><b>Clara Windham</b><small>38 today</small></div></div>
      <div class="person"><div class="avatar" role="img" aria-label="Portrait of Amanda Rusk" style="background:#9a7060"></div><div><b>Amanda Rusk</b><small>32 today</small></div></div>
    </div>
  </section>

  <aside class="side">
    <div class="ad">
      <div class="ad-brand" style="color:var(--pink)">Lumelle</div>
      <div class="grid">
        <div role="img" aria-label="Fashion dress photo" style="background:linear-gradient(#f2c6d2,#d9768f)"></div>
        <div role="img" aria-label="Fashion dress photo" style="background:linear-gradient(#e9e4ef,#9aa6c8)"></div>
        <div role="img" aria-label="Fashion dress photo" style="background:linear-gradient(#2b2b3a,#6a5a7a)"></div>
        <div role="img" aria-label="Fashion dress photo" style="background:linear-gradient(#f4f0ea,#d6cfc4)"></div>
      </div>
      <div style="font-size:14px;font-weight:700;color:var(--ink);margin-top:12px">FREE SHIPPING $79+</div>
      <span class="cta">VIEW MORE ›</span>
    </div>
    <div class="ad fly">
      <div style="font-size:14px;font-weight:700;color:var(--ink)">US</div>
      <div class="big">$99</div>
      <div style="font-size:18px;font-weight:700;color:var(--ink);margin-top:6px">Super Cheap Flights</div>
      <span class="cta" style="margin-top:14px">Find Deals</span>
    </div>
    <div class="ad" style="padding:18px 0 22px">
      <div class="ad-brand" style="color:var(--ink);padding:0">Castellin</div>
      <div style="font-size:11px;letter-spacing:2px;color:var(--muted)">UNLIKE ANY OTHER RING</div>
      <div role="img" aria-label="Engagement ring photo" style="width:120px;height:70px;margin:14px auto 0;background:linear-gradient(135deg,#f4f4f4,#c9c9c9)"></div>
    </div>
  </aside>
</main>

<div class="foot-ad"><div class="brand">Adventa</div><div class="copy"><b>PERSONALIZED EXPERIENCES FOR EVERY VISITOR</b><small>MACHINE LEARNING FOR PUBLISHERS</small></div></div>
<div class="share">SHARE <i></i><i></i><i></i><i></i></div>
<div class="links">Terms and Conditions | Privacy Policy | © 2018 Marlo Vista | www.marlovista.com</div>
</body>
</html>
```